https://copperwillowbrambleyard.org/

We would like the website to represent 19th century African American civil war soldier's letters. We would like the site colors to be nice and clean . Along with the layout, including a great landing page , blogs and introduction.

```html
<!DOCTYPE html>
<html lang="en">
<head>
<meta charset="utf-8">
<title>Copper Willow Bramble Yard</title>
<link rel="stylesheet" href="https://fonts.googleapis.com/css2?family=Cinzel:wght@700;900&family=Oswald:wght@500;600;700&family=Roboto:ital,wght@0,400;1,400;1,500&display=swap">
<style>
:root{
  --parchment:#f2d49a;
  --parchment-light:#f7dfae;
  --panel:#f8e2b8;
  --card:#f6e3c0;
  --ink:#3a1f0c;
  --ink-soft:#4a2e18;
  --body:#3c2a1c;
  --rule:#3a1f0c;
  --amber:#d99a3c;
  --sepia-dark:#3b2614;
  --sepia-mid:#7a5634;
  --sepia-light:#b58c5e;
  --cream:#fbebcf;
}
*{box-sizing:border-box;margin:0;padding:0}
html,body{width:1200px;height:2371px;overflow:hidden}
body{
  position:relative;
  background:
    radial-gradient(ellipse at 20% 10%,rgba(255,230,170,.55),transparent 55%),
    radial-gradient(ellipse at 85% 60%,rgba(235,185,110,.35),transparent 60%),
    radial-gradient(ellipse at 10% 80%,rgba(240,195,120,.35),transparent 55%),
    var(--parchment);
  font-family:"Roboto",sans-serif;color:var(--body);
}
.abs{position:absolute}

/* header */
.brand{left:173px;top:15px;display:flex;align-items:center;gap:13px}
.brand-mark{width:80px;height:59px;background:linear-gradient(135deg,#8a5a2e,#c79a62 60%,#6b3f1d)}
.brand-name{font-family:"Cinzel",serif;font-weight:900;font-size:18px;line-height:22px;color:var(--ink);letter-spacing:.5px}
.main-nav{top:33px;left:627px;display:flex;gap:0}
.main-nav a{position:absolute;font-family:"Oswald",sans-serif;font-weight:600;font-size:17px;color:var(--ink);text-decoration:none;white-space:nowrap}
.search{left:994px;top:29px;width:32px;height:32px;border-radius:50%;background:var(--ink)}

/* hero */
.hero{left:171px;top:95px;width:858px;height:529px;border-radius:22px;
  border:4px solid var(--cream);
  background:radial-gradient(ellipse at 60% 40%,var(--sepia-light),var(--sepia-mid) 45%,var(--sepia-dark) 100%);
  box-shadow:0 0 0 2px rgba(251,235,207,.5)}
.hero-frame{left:196px;top:119px;width:809px;height:481px;border:2px solid #fff3dc;border-radius:20px}
.hero-title{left:171px;top:284px;width:858px;text-align:center;font-family:"Oswald",sans-serif;font-weight:700;font-size:55px;line-height:61px;color:#f7e3b8;text-transform:uppercase;text-shadow:0 2px 6px rgba(0,0,0,.8)}
.hero-dots{left:512px;top:564px;display:flex;gap:4px}
.hero-dots span{width:41px;height:4px;background:#fff}
.hero-dots span.off{background:transparent;border:1px solid #fff}

/* section headings */
.rule{left:171px;width:855px;height:5px;border-top:2px solid var(--rule);border-bottom:1px solid var(--rule)}
.section-title{left:171px;width:858px;text-align:center;font-family:"Oswald",sans-serif;font-weight:600;font-size:37px;letter-spacing:4.6px;color:var(--ink);text-transform:uppercase}

/* intro */
.intro-photo{left:175px;top:791px;width:414px;height:354px;border-radius:22px;border:4px solid var(--amber);
  background:linear-gradient(135deg,#c9a173,#6e4a2c 50%,#2e1d10)}
.intro-text{left:613px;top:793px;width:414px;height:348px;border-radius:22px;background:var(--panel);
  box-shadow:0 2px 10px rgba(120,80,30,.2);padding:38px 30px 0 43px;font-size:14.6px;line-height:26.2px;color:var(--body)}

/* cards */
.card{top:1337px;width:268px;height:487px;background:var(--card);box-shadow:0 2px 8px rgba(120,80,30,.25)}
.card-photo{height:206px}
.card-body{padding:25px 20px 0 20px}
.card-title{font-family:"Oswald",sans-serif;font-weight:500;font-size:17.5px;line-height:27px;color:var(--ink);text-transform:uppercase;margin-left:0}
.card-excerpt{margin-top:10px;font-size:12.6px;line-height:21px;color:var(--body);padding-left:2px}
.card-meta{margin-top:18px;font-size:11.8px;color:var(--body);padding-left:2px}
.card-meta a{color:var(--body);margin-right:12px}

/* quote */
.quote{left:171px;top:1940px;width:858px;text-align:center;font-style:italic;font-weight:500;font-size:22px;line-height:34px;color:var(--ink-soft)}
.quote-cite{left:171px;top:2070px;width:858px;text-align:center;font-family:"Oswald",sans-serif;font-weight:600;font-size:22px;color:var(--ink)}

/* footer */
.social{top:2188px;width:32px;height:32px;border-radius:50%;border:2px solid var(--ink)}
.footer-nav{left:0;top:2244px;width:1200px;text-align:center}
.footer-nav a{font-family:"Oswald",sans-serif;font-weight:600;font-size:17px;color:var(--ink);text-decoration:none;margin:0 7px}
.copyright{left:0;top:2299px;width:1200px;text-align:center;font-size:15px;color:var(--ink)}
.copyright a{color:var(--ink);text-decoration:none;margin-left:12px}
</style>
</head>
<body>

<header>
  <div class="abs brand">
    <div class="brand-mark" role="img" aria-label="Square of sepia tone beside the site name"></div>
    <div class="brand-name">Copper Willow<br>Bramble Yard</div>
  </div>
  <nav class="abs main-nav" style="left:0;top:33px">
    <a href="#" style="left:627px">ABOUT</a>
    <a href="#" style="left:711px">BLOG</a>
    <a href="#" style="left:785px">CONTACT</a>
    <a href="#" style="left:883px">BLOG FEED</a>
  </nav>
  <div class="abs search" aria-label="Search">
    <svg width="32" height="32" viewBox="0 0 32 32"><circle cx="14.5" cy="14.5" r="5.5" fill="none" stroke="#f6e3c0" stroke-width="2"/><line x1="18.5" y1="18.5" x2="22.5" y2="22.5" stroke="#f6e3c0" stroke-width="2.2" stroke-linecap="round"/></svg>
  </div>
</header>

<section>
  <div class="abs hero" role="img" aria-label="Sepia photograph of Civil War soldiers resting in a trench"></div>
  <div class="abs hero-frame"></div>
  <h1 class="abs hero-title">Copper Willow<br>Bramble Yard</h1>
  <div class="abs hero-dots"><span></span><span></span><span class="off"></span><span></span></div>
</section>

<section>
  <div class="abs rule" style="top:674px"></div>
  <h2 class="abs section-title" style="top:685px">Welcome to Copper Willow Bramble Yard</h2>
  <div class="abs rule" style="top:738px"></div>

  <div class="abs intro-photo" role="img" aria-label="Scattered old letters and sepia family photographs"></div>
  <div class="abs intro-text">
    As the third great granddaughter of Pvt. Elias Harrow, who escaped enslavement from a Louisa, Virginia plantation in 1863 to join the 29th Illinois Colored Infantry, she is interested in the merging of genealogical and archival information to more deeply understand the lives of black Civil War servicemen before and after the war. She has several published articles and encyclopedia entries; has presented at various local, state, and national conferences; and has presented at local museums, research centers, and universities.
  </div>
</section>

<section>
  <div class="abs rule" style="top:1225px"></div>
  <h2 class="abs section-title" style="top:1236px">Latest Blog Posts</h2>
  <div class="abs rule" style="top:1290px"></div>

  <article class="abs card" style="left:173px">
    <div class="card-photo" role="img" aria-label="Old handwritten letters and photographs spread on a table" style="background:linear-gradient(135deg,#c89a6a,#7a4a28 55%,#3a2414)"></div>
    <div class="card-body">
      <h3 class="card-title">"I'm well and doing well as a soldier can expect..."</h3>
      <p class="card-excerpt">Tobin's ninth letter in this collection was written December 29th, 1864 while he and his regiment were in Beaufort, South Carolina. His letter opens with acknowledging the receipt of his mother's last letter. {..}</p>
      <p class="card-meta">by <a href="#">mwillow22</a>February 16, 2020</p>
    </div>
  </article>

  <article class="abs card" style="left:466px">
    <div class="card-photo" role="img" aria-label="Soldiers marching through a snowy forest" style="background:linear-gradient(180deg,#6e4a3c,#a88878 45%,#e8dcd6)"></div>
    <div class="card-body">
      <h3 class="card-title">"I have not heard from brother John since....</h3>
      <p class="card-excerpt">Tobin's ninth letter in this collection was written December 29th, 1864 while he and his regiment were in Beaufort, South Carolina. His letter opens with acknowledging the receipt of his mother's last letter. {..}</p>
      <p class="card-meta">by <a href="#">mwillow22</a>February 16, 2020</p>
    </div>
  </article>

  <article class="abs card" style="left:759px">
    <div class="card-photo" role="img" aria-label="Antique express shipping receipts and orange tickets" style="background:linear-gradient(120deg,#e8dccf,#c9b6a4 45%,#d9772c 70%,#5a2a14)"></div>
    <div class="card-body">
      <h3 class="card-title">Freedom by sword and<br>open...</h3>
      <p class="card-excerpt">Tobin's ninth letter in this collection was written December 29th, 1864 while he and his regiment were in Beaufort, South Carolina. His letter opens with acknowledging the receipt of his mother's last letter. {..}</p>
      <p class="card-meta">by <a href="#">mwillow22</a>February 16, 2020</p>
    </div>
  </article>
</section>

<section>
  <div class="abs rule" style="top:1907px"></div>
  <blockquote class="abs quote">“Do not forget the things your eyes have seen or let them<br>slip from your heart as long as you live. Teach them to<br>your children and your children’s children.”</blockquote>
  <p class="abs quote-cite">— DEUTERONOMY 4:9.</p>
  <div class="abs rule" style="top:2144px"></div>
</section>

<footer>
  <a class="abs social" href="#" style="left:564px" aria-label="Social profile one"></a>
  <a class="abs social" href="#" style="left:602px" aria-label="Social profile two"></a>
  <nav class="abs footer-nav">
    <a href="#">ABOUT</a><a href="#">BLOG</a><a href="#">CONTACT</a><a href="#">BLOG FEED</a>
  </nav>
  <p class="abs copyright">Copyright © 2020 All Rights reserved. <a href="#" style="margin-left:0">Privacy Policy</a><a href="#">Terms &amp; Conditions</a></p>
</footer>

</body>
</html>
```